Business Cards/Stationery - Information Technology Company
Dale Porvin Advisory, An Information Technology Services Company
Business Cards/Stationery - Information Technology Company - Information Technology
Creative Brief
Use specific fonts
Whatever works the best.
Simple
Dale Porvin
Solutions Architect & Owner
928 Tarrow Street Suite 504 Glen Ellyn, IL 60139-8812
daleporvin@mailbright.example
http://daleporvin.example
Please use the tagline: "An Information Technology Services Company" under the logo on cards, letterhead, and envelope.
daleporvin daleporvin
Sorry about the long delay. I will be selecting a finalist in the next day.
The NPDX uses the bottom 1/2" of envelopes and prints a black barcode and text when processing. This area should be either be left blank or printed with very light colors or watermark. Designs can have printing on the bottom 1/2" of envelopes as long as it is light enough that NPDX can print its black barcode and it will be visible.
I will rate all designs very soon. Thanks for your patience.
QUIKMAKRR QUIKMAKRR
Star rating please,,,
The two color logo in .ai format has been uploaded and is now available to designers. Sorry about the delay.
The two logo in .ai format has been uploaded and is now available to designers. Sorry about the delay.
I really like the two sided designs that have been submitted so far. I didn't originally plan on a two sided design, but I have changed my mind thanks to all the designer's excellent work. PLEASE SUBMIT ALL FUTURE DESIGNS AS TWO SIDED. Thanks!
ninerock ninerock
Please upload Ai file of your logo!! thnks
I just uploaded the two color version of the logo in .jpg format. I also have .psd and .tif formats available. I don't have an .ai version, but I can get if needed. Please use the two color logo version and let me know if you need anything else. Thanks!

```html
<!DOCTYPE html>
<html lang="en">
<head>
<meta charset="utf-8">
<title>Dale Porvin Advisory – Business Card</title>
<link rel="stylesheet" href="https://fonts.googleapis.com/css2?family=PT+Sans+Narrow:wght@400;700&family=PT+Sans:wght@400;700&display=swap">
<style>
  :root {
    --backdrop: #2c2d2f;
    --card-light: #ffffff;
    --card-shade: #e4e5e8;
    --navy: #1f3a6e;
    --band-blue: #2b4d8c;
    --swoosh-grey: #8d8f93;
    --text-grey: #4a4b4e;
    --muted-grey: #9a9ca0;
  }
  * { box-sizing: border-box; margin: 0; padding: 0; }
  html, body { width: 1200px; height: 1099px; overflow: hidden; }
  body {
    background: var(--backdrop);
    position: relative;
    font-family: "PT Sans", Arial, sans-serif;
  }
  .card {
    position: absolute;
    border-radius: 20px;
    overflow: hidden;
    background: linear-gradient(135deg, var(--card-light) 0%, var(--card-light) 45%, var(--card-shade) 100%);
  }
  .card-front { left: 352px; top: 110px; width: 706px; height: 406px; }
  .card-back  { left: 155px; top: 590px; width: 697px; height: 393px; }

  .brand {
    position: absolute;
    display: flex;
    align-items: center;
  }
  .brand-square {
    background: var(--navy);
    border-radius: 6px;
    flex: none;
  }
  .brand-name {
    font-family: "PT Sans Narrow", "Arial Narrow", sans-serif;
    font-weight: 400;
    color: var(--navy);
    line-height: 0.98;
  }
  .tagline {
    position: absolute;
    font-family: "PT Sans Narrow", "Arial Narrow", sans-serif;
    font-weight: 700;
    color: var(--navy);
    white-space: nowrap;
  }

  /* front */
  .card-front .brand { left: 58px; top: 108px; gap: 44px; }
  .card-front .brand-square { width: 92px; height: 92px; }
  .card-front .brand-name { font-size: 50px; }
  .card-front .tagline { left: 52px; top: 272px; font-size: 22px; }
  .front-web {
    position: absolute; left: 0; width: 470px; top: 328px;
    text-align: center; font-size: 15px; color: var(--text-grey);
  }
  .front-tm {
    position: absolute; right: 48px; bottom: 20px;
    font-size: 14px; color: var(--muted-grey); letter-spacing: 1px;
  }

  /* back */
  .back-band { position: absolute; inset: 0; }
  .card-back .brand { left: 112px; top: 108px; gap: 38px; }
  .card-back .brand-square { width: 68px; height: 68px; }
  .card-back .brand-name { font-size: 40px; }
  .card-back .tagline { left: 108px; top: 234px; font-size: 16.5px; }
  .holder {
    position: absolute; right: 40px; top: 36px; text-align: right;
  }
  .holder-name {
    font-weight: 700; font-size: 22px; color: var(--navy);
  }
  .holder-title { font-size: 11.5px; color: var(--text-grey); margin-top: 2px; }
  .contact {
    position: absolute; right: 26px; top: 238px;
    text-align: right; font-size: 14.5px; color: var(--text-grey);
    line-height: 1.42;
  }
  .contact-line { display: flex; justify-content: flex-end; align-items: center; gap: 8px; }
  .contact-icon { width: 14px; height: 14px; flex: none; }
  .contact-plain { padding-right: 22px; }
</style>
</head>
<body>

  <section class="card card-front" aria-label="Card front">
    <div class="brand">
      <span class="brand-square"></span>
      <span class="brand-name">Dale<br>Porvin<br>Advisory</span>
    </div>
    <p class="tagline">“An Information Technology Services Company”</p>
    <p class="front-web">www.daleporvin.example</p>
    <span class="front-tm">TM</span>
  </section>

  <section class="card card-back" aria-label="Card back">
    <svg class="back-band" width="697" height="393" viewBox="0 0 697 393" aria-hidden="true">
      <path d="M0 0 H165 C95 70 62 210 66 393 H0 Z" fill="var(--swoosh-grey)"/>
      <path d="M0 0 H105 C50 85 26 220 22 393 H0 Z" fill="var(--band-blue)"/>
    </svg>
    <div class="holder">
      <p class="holder-name">Dale Porvin</p>
      <p class="holder-title">Solutions Architect &amp; Owner</p>
    </div>
    <div class="brand">
      <span class="brand-square"></span>
      <span class="brand-name">Dale<br>Porvin<br>Advisory</span>
    </div>
    <p class="tagline">“An Information Technology Services Company”</p>
    <div class="contact">
      <p class="contact-plain">928 Tarrow Street, Suite 504</p>
      <p class="contact-plain">Brackenridge, OR 60139-8812</p>
      <p class="contact-line">555-301-0148
        <svg class="contact-icon" viewBox="0 0 14 14" aria-hidden="true"><circle cx="7" cy="7" r="6.5" fill="none" stroke="var(--text-grey)"/><path d="M4.5 3.5 L6 3.5 L6.5 5.5 L5.6 6.2 C6.2 7.4 6.8 8 7.8 8.4 L8.5 7.5 L10.5 8 L10.5 9.5 C7 10 4 7 4.5 3.5 Z" fill="var(--text-grey)"/></svg>
      </p>
      <p class="contact-line">daleporvin@mailbright.example
        <svg class="contact-icon" viewBox="0 0 14 14" aria-hidden="true"><rect x="1" y="3" width="12" height="8" fill="none" stroke="var(--text-grey)"/><path d="M1 3 L7 8 L13 3" fill="none" stroke="var(--text-grey)"/></svg>
      </p>
      <p class="contact-line">www.daleporvin.example
        <svg class="contact-icon" viewBox="0 0 14 14" aria-hidden="true"><circle cx="7" cy="7" r="6" fill="none" stroke="var(--text-grey)"/><ellipse cx="7" cy="7" rx="2.6" ry="6" fill="none" stroke="var(--text-grey)"/><path d="M1 7 H13" stroke="var(--text-grey)"/></svg>
      </p>
    </div>
  </section>

</body>
</html>
```